Bref créative
Business Cards and Stationary for General Contractor
Velmarosh Building, LLC.
I need double sided standard sized Business Card [3.5" x 2"]
Standard Fonts or use use same font as used in logo
Professional
Colton Prewitt
Project Manager
2176 Harlow B Loop
colton@velmarosh-example.com
www.velmarosh-example.com
Used fonts as recommended. Need Biz Cards, Letterheads, Envelopes.
Use logo. If want to change the way Velmarosh Building is displayed that's ok or leave as is.
white VB logo with green background with web address. Other ideas as suggested.

```html
<!DOCTYPE html>
<html lang="en">
<head>
<meta charset="utf-8">
<title>Velmarosh Building, LLC. — Stationery Set</title>
<link href="https://fonts.googleapis.com/css2?family=Montserrat:wght@500;800&family=Open+Sans:wght@400;600&display=swap" rel="stylesheet">
<style>
  :root{
    --stage:#e9e4dc;
    --paper:#ffffff;
    --green:#2f9a3a;
    --green-dark:#1f7a2a;
    --green-light:#8fd06a;
    --grey:#6a6a6a;
    --grey-dark:#4a4a4a;
    --ink:#3a3a3a;
    --faint:#eef5ea;
  }
  *{box-sizing:border-box;margin:0;padding:0}
  html,body{width:1200px;height:446px;overflow:hidden}
  body{background:var(--stage);position:relative;font-family:"Open Sans",Arial,sans-serif;color:var(--ink)}
  .sheet{position:absolute;background:var(--paper);box-shadow:0 2px 6px rgba(0,0,0,.18);overflow:hidden}
  .label{position:absolute;font-size:7px;letter-spacing:.5px;color:var(--grey-dark);text-align:center;white-space:nowrap;font-family:"Open Sans",Arial,sans-serif}
  .brand{display:flex;align-items:center;gap:4px}
  .brand-mark{background:var(--green);flex:none}
  .brand-name{font-family:"Montserrat",Arial,sans-serif;font-weight:800;color:var(--green);line-height:1;text-transform:uppercase}
  .brand-name small{display:block;font-size:.55em;letter-spacing:.3px}
  .faint-circle{position:absolute;border-radius:50%;background:var(--faint)}
  .contact{position:absolute;font-size:4px;line-height:6.5px;color:var(--grey)}
  .contact span{display:flex;align-items:center;gap:2px;white-space:nowrap}
  .contact span::before{content:"";width:3px;height:3px;background:var(--green);display:block;flex:none}

  .stage-title{left:14px;top:122px;width:80px;text-align:left}

  .card-front{left:19px;top:160px;width:74px;height:42px;padding:5px 5px}
  .card-front .brand-mark{width:8px;height:8px}
  .card-front .brand-name{font-size:6px}
  .card-front .person{margin-top:3px;font-size:3.6px;line-height:4.4px;color:var(--ink);font-weight:600}
  .card-front .person em{font-style:normal;font-weight:400;color:var(--grey)}
  .card-front .contact{left:5px;bottom:3px;font-size:2.9px;line-height:3.8px}
  .card-front .contact span::before{width:2px;height:2px}
  .card-front .faint-circle{width:34px;height:34px;right:-8px;bottom:-10px}

  .card-back{left:19px;top:240px;width:74px;height:42px;background:linear-gradient(var(--green-light),var(--green));display:flex;flex-direction:column;align-items:center;justify-content:center;gap:4px}
  .card-back .brand-mark{width:7px;height:7px;background:#fff}
  .card-back .brand-name{font-size:6px;color:#fff}
  .card-back .web{font-size:3.4px;color:#fff;letter-spacing:.2px}

  .letterhead{top:16px;width:292px;height:400px;padding:14px 18px}
  .lh-1{left:163px}
  .lh-2{left:476px}
  .letterhead .brand-mark{width:14px;height:14px}
  .letterhead .brand-name{font-size:11px}
  .letterhead .contact{right:18px;top:14px}
  .letterhead .faint-circle{width:150px;height:150px;left:71px;top:180px}
  .footer-band{position:absolute;left:0;right:0;bottom:10px;height:12px;background:linear-gradient(var(--green-light),var(--green))}
  .footer-band p{font-size:3.5px;color:#fff;text-align:center;line-height:12px;letter-spacing:.4px}

  .envelope-stack{position:absolute;left:840px;top:10px;width:355px;height:240px}
  .env{position:absolute;left:0;width:355px;height:150px;background:var(--paper);box-shadow:0 2px 5px rgba(0,0,0,.18);overflow:hidden}
  .env-green{top:0}
  .env-grey{top:40px}
  .env-white{top:88px}
  .env svg{position:absolute;left:0;top:0}
  .env-white .brand{position:absolute;left:165px;top:98px}
  .env-white .brand-mark{width:16px;height:16px;background:var(--green-dark)}

  .env-front{left:835px;top:276px;width:345px;height:144px;padding:14px 16px}
  .env-front .brand-mark{width:12px;height:12px}
  .env-front .brand-name{font-size:9px}
  .env-front .return{font-size:4px;color:var(--grey);margin-top:4px}
  .env-front .footer-band{bottom:12px;height:10px}
</style>
</head>
<body>
  <p class="label stage-title">Stationery Samples</p>

  <div class="sheet card-front">
    <div class="faint-circle"></div>
    <div class="brand"><span class="brand-mark"></span><span class="brand-name">Velmarosh<small>Building, LLC.</small></span></div>
    <p class="person">Colton Prewitt<br><em>Project Manager</em></p>
    <div class="contact"><span>2176 Harlow B Loop</span><span>colton@velmarosh-example.com</span><span>www.velmarosh-example.com</span></div>
  </div>
  <p class="label" style="left:19px;top:206px;width:74px">Business Card Front</p>

  <div class="sheet card-back">
    <div class="brand"><span class="brand-mark"></span><span class="brand-name">Velmarosh</span></div>
    <p class="web">www.velmarosh-example.com</p>
  </div>
  <p class="label" style="left:19px;top:286px;width:74px">Business Card Back</p>

  <div class="sheet letterhead lh-1">
    <div class="brand"><span class="brand-mark"></span><span class="brand-name">Velmarosh<small>Building, LLC.</small></span></div>
    <div class="contact"><span>2176 Harlow B Loop</span><span>colton@velmarosh-example.com</span><span>www.velmarosh-example.com</span><span>Colton Prewitt</span></div>
    <div class="faint-circle"></div>
  </div>
  <p class="label" style="left:163px;top:422px;width:292px">Letterhead Option 1</p>

  <div class="sheet letterhead lh-2">
    <div class="brand"><span class="brand-mark"></span><span class="brand-name">Velmarosh<small>Building, LLC.</small></span></div>
    <div class="faint-circle"></div>
    <div class="footer-band"><p>2176 Harlow B Loop &nbsp;•&nbsp; colton@velmarosh-example.com &nbsp;•&nbsp; www.velmarosh-example.com</p></div>
  </div>
  <p class="label" style="left:476px;top:422px;width:292px">Letterhead Option 2</p>

  <div class="envelope-stack">
    <div class="env env-green">
      <svg width="355" height="60" viewBox="0 0 355 60"><defs><linearGradient id="gflap" x1="0" y1="0" x2="0" y2="1"><stop offset="0" stop-color="#8fd06a"/><stop offset="1" stop-color="#2f9a3a"/></linearGradient></defs><path d="M0 0H355V30Q330 46 300 48H55Q25 46 0 30Z" fill="url(#gflap)"/></svg>
    </div>
    <div class="env env-grey">
      <svg width="355" height="60" viewBox="0 0 355 60"><defs><linearGradient id="grflap" x1="0" y1="0" x2="0" y2="1"><stop offset="0" stop-color="#9a9a9a"/><stop offset="1" stop-color="#4a4a4a"/></linearGradient></defs><path d="M0 0H355V30Q330 46 300 48H55Q25 46 0 30Z" fill="url(#grflap)"/></svg>
    </div>
    <div class="env env-white">
      <svg width="355" height="80" viewBox="0 0 355 80"><path d="M0 0L150 60Q177 70 205 60L355 0" fill="none" stroke="#d8d8d8" stroke-width="1"/></svg>
      <div class="brand"><span class="brand-mark"></span></div>
    </div>
  </div>

  <div class="sheet env-front">
    <div class="brand"><span class="brand-mark"></span><span class="brand-name">Velmarosh<small>Building, LLC.</small></span></div>
    <p class="return">2176 Harlow B Loop</p>
    <div class="footer-band"></div>
  </div>
  <p class="label" style="left:835px;top:424px;width:345px">Envelope Option 3</p>
</body>
</html>
```